Marlow Pike PPT 1

I need a PPT template that I could apply to several uses both internally and externally.
Marlow Pike is not a new company but rather a new spin-off from my previous brand. We are a Business Consulting firm known for our ability implement the advice we provide our clients and see it through to fruition. The vast majority of our projects involve IT or software technology. Particularly with new software implementations, software integrations arising from a merger or acquisition. We consult to almost every industry except Mining, construction and agriculture but mostly for Financial Services, automotive and Hospitality services. We offer a tailored service through trusted, longstanding relationships with our clients.
From a look, feel and overall theme perspective, Pike is the Viking god of war but, more importantly, he is known for his WISDOM, ADAPATABILITY, RESILENCE. He is in fact a shape shifter. We chose Pike because we advise our clients on ways to remain Agile and adaptable to rapidly changing environments to remain competitive now and in the future.
The word steel was added to denote strength, reliability sustainability.
I have recently run a logo design competition for the new logo.

I would like an all-purpose PPT template that is crisp, clean, uncomplicated but professional and attractive to the eye.
I am keen to see some ideas.
Thanks
Dana

```html
<!DOCTYPE html>
<html lang="en">
<head>
<meta charset="utf-8">
<title>Marlow Pike — Presentation Template</title>
<link href="https://fonts.googleapis.com/css2?family=Montserrat:ital,wght@0,400;0,500;0,600;0,700;0,800;1,600&display=swap" rel="stylesheet">
<style>
:root{
  --board:#58595b;
  --red:#c8102e;
  --red-dark:#9d0b21;
  --ink:#222;
  --title:#5d5d5f;
  --grey:#8a8a8c;
  --light:#ececec;
  --white:#fff;
  --dark:#1c1c1e;
}
*{margin:0;padding:0;box-sizing:border-box}
html,body{width:1200px;height:2806px;overflow:hidden}
body{background:var(--board);font-family:"Montserrat",sans-serif;color:var(--ink);position:relative}
.slide{position:absolute;width:439px;height:246px;background:var(--white);overflow:hidden;box-shadow:0 6px 14px rgba(0,0,0,.35)}
.col-l{left:149px}.col-r{left:613px}
.slide.framed{border-top:2px solid var(--red);border-bottom:2px solid var(--red)}
.brand-mini{position:absolute;top:10px;right:12px;font-size:7px;font-weight:700;color:#6b6b6d;letter-spacing:.5px;line-height:1;z-index:2}
.s-title{position:absolute;left:22px;top:10px;font-size:19px;font-weight:800;color:var(--title);letter-spacing:.4px;line-height:1.05;z-index:2}
.rule{position:absolute;height:1px;background:var(--red);z-index:2}
.rule::after{content:"";position:absolute;right:-3px;top:-2.5px;width:6px;height:6px;border-radius:50%;background:var(--red)}
.footer{position:absolute;left:22px;bottom:8px;font-size:5.5px;color:var(--red);font-weight:500;z-index:2}
.page{position:absolute;right:6px;bottom:6px;width:15px;height:15px;border-radius:50%;background:var(--red);color:#fff;font-size:6px;font-weight:700;display:flex;align-items:center;justify-content:center;box-shadow:0 0 0 2px #fff,0 0 0 3px #bbb;z-index:2}
.body-text{position:absolute;font-size:7px;line-height:1.6;color:#555;text-align:justify;z-index:2}
.deco{position:absolute;border-radius:50%;z-index:0}
.deco-soft{background:radial-gradient(circle at 60% 55%,#f3d6da 0 18%,#f2f2f2 19% 55%,rgba(255,255,255,0) 70%)}
.deco-dark{background:radial-gradient(circle at 62% 58%,var(--red) 0 14%,#2a2a2c 15% 45%,#cfcfcf 46% 60%,rgba(255,255,255,0) 72%)}
.big-title{position:absolute;font-size:19px;font-weight:800;color:var(--title);z-index:2}
/* cover */
.cover{background:linear-gradient(135deg,#2b2b2d,#121214 60%,#2a2a2c)}
.cover .brand{position:absolute;left:38px;top:48px;font-size:30px;font-weight:800;color:#bdbdbf;line-height:1;letter-spacing:1px}
.cover .tag{position:absolute;left:38px;top:153px;font-size:19px;font-weight:800;color:#fff;line-height:1.3}
.cover .tag em{font-style:normal;color:var(--red)}
.cover .wave{position:absolute;right:0;bottom:0;width:300px;height:180px;background:radial-gradient(ellipse at 70% 60%,rgba(160,160,160,.25),rgba(0,0,0,0) 65%)}
/* agenda */
.agenda-list{position:absolute;left:92px;top:52px;list-style:none}
.agenda-list li{display:flex;align-items:center;height:34.5px;font-size:8px;font-weight:500;color:#333}
.agenda-list .num{width:14px;height:14px;border-radius:50%;background:var(--red);color:#fff;font-size:5.5px;font-weight:700;display:flex;align-items:center;justify-content:center;margin-right:16px;box-shadow:0 0 0 2px #fff,-6px 0 0 2px #d8d8d8}
/* features */
.feature{position:absolute;font-size:7px;font-weight:600;line-height:1.55;text-align:right;color:#333;z-index:2}
.feat-icon{position:absolute;width:26px;height:26px;border-radius:50%;display:flex;align-items:center;justify-content:center;z-index:3}
/* team photo */
.photo{position:absolute}
/* team cards */
.cards{position:absolute;left:20px;top:70px;display:flex;gap:5px}
.card{width:75px;height:70px;background:#f1f1f1;border:1px solid #ddd;display:flex;flex-direction:column;align-items:center;padding-top:8px}
.card.active{background:#8d8d8f}
.avatar{width:34px;height:34px;border-radius:50%;background:linear-gradient(#9a9a9c,#3e3e40)}
.card .name{font-size:5.5px;font-weight:700;margin-top:7px;color:#222}
.card.active .name{color:#fff}
.card .role{font-size:4px;font-weight:600;color:#444}
.card-desc{width:75px;font-size:4.2px;line-height:1.5;color:#666;text-align:center;margin-top:6px}
.descs{position:absolute;left:20px;top:149px;display:flex;gap:5px}
/* quote */
.quote-slide{background:linear-gradient(135deg,#9c9c9e,#707072)}
.quote-text{position:absolute;left:95px;top:85px;width:265px;font-size:9px;font-style:italic;font-weight:600;color:#fff;text-align:center;line-height:1.6}
.qmark{position:absolute;font-size:22px;font-weight:800;color:var(--red);line-height:1}
/* chart */
.chart{position:absolute;left:36px;top:105px;width:360px;height:100px}
.axis{position:absolute;left:0;top:0;height:100px;display:flex;flex-direction:column;justify-content:space-between;font-size:4px;color:#666}
.bars{position:absolute;left:25px;top:0;right:0;height:100px;display:flex;justify-content:space-between}
.bar{width:14px;height:100px;background:#dcdcdc;position:relative}
.bar span{position:absolute;left:0;bottom:0;width:100%;background:#2a2a2c;color:#fff;font-size:3.5px;text-align:center;padding-top:3px}
.bar span.hl{background:var(--red)}
/* timeline */
.tl-node{position:absolute;top:104px;width:42px;height:42px;border-radius:50%;background:#fff;box-shadow:0 2px 5px rgba(0,0,0,.25);border:3px solid var(--red);display:flex;align-items:center;justify-content:center}
.tl-node.alt{border-color:#cfcfcf}
.tl-label{position:absolute;font-size:4.5px;font-weight:700;text-align:center;line-height:1.4;width:80px;color:#222}
.tl-stem{position:absolute;width:1px;background:#444}
/* infographics */
.info-box{position:absolute;top:80px;width:90px;height:133px;border:2px solid #9a9a9c;border-radius:12px;text-align:center;padding-top:12px;background:#fff}
.info-box h4{font-size:6.5px;font-weight:600;color:var(--red);margin-top:5px}
.info-box p{font-size:4.4px;line-height:1.6;color:#666;padding:4px 10px 0}
/* what we do */
.wwd-panel{position:absolute;left:0;top:0;width:230px;height:246px;background:linear-gradient(180deg,#2f2f31,#6b6b6d 60%,#9a9a9c)}
.wwd-item{position:absolute;font-size:5.6px;line-height:1.5}
.wwd-item h5{font-size:7px;font-weight:700;margin-bottom:2px}
.wwd-ico{position:absolute;width:22px;height:22px;border-radius:50%;display:flex;align-items:center;justify-content:center}
/* thank you */
.thanks-grey{background:linear-gradient(135deg,#4a4a4c,#2e2e30)}
.thanks-red{background:linear-gradient(135deg,#b00d25,#d21a33 60%,#a30c22)}
.contact-row{position:absolute;left:26px;display:flex;align-items:center;font-size:6.5px;color:#fff;font-weight:500}
.contact-row i{width:17px;height:17px;border-radius:50%;background:#fff;display:flex;align-items:center;justify-content:center;margin-right:14px}
</style>
</head>
<body>

<!-- 1 Cover -->
<section class="slide col-l cover" style="top:97px">
  <div class="wave" role="img" aria-label="Soft dotted wave texture"></div>
  <div class="brand">MARLOW<br>PIKE</div>
  <div class="rule" style="left:38px;top:136px;width:245px"></div>
  <p class="tag">WISDOM, <em>ADAPATABILITY</em><br>RESILENCE</p>
</section>

<!-- 2 Features & Benefits -->
<section class="slide col-r framed" style="top:97px">
  <div class="deco deco-dark" style="left:250px;top:-10px;width:230px;height:250px" role="img" aria-label="Large decorative emblem with red accent"></div>
  <h2 class="s-title" style="top:6px">FEATURES &amp;<br>BENEFITS</h2>
  <div class="rule" style="left:0;top:60px;width:160px"></div>
  <span class="brand-mini">MARLOW PIKE</span>
  <p class="feature" style="left:16px;top:88px;width:145px">Nemo enim ipsam voluptatem quia voluptas sit aspernatur aut odit aut fugit, sed quia consequuntur magni dolores eos qui ratione</p>
  <div class="feat-icon" style="left:166px;top:86px;background:var(--red)"><svg width="11" height="10" viewBox="0 0 11 10"><rect x="1" y="1" width="9" height="6" fill="none" stroke="#fff" stroke-width="1.2"/><path d="M4 9h3" stroke="#fff"/></svg></div>
  <p class="feature" style="left:62px;top:148px;width:145px">Nemo enim ipsam voluptatem quia voluptas sit aspernatur aut odit aut fugit, sed quia consequuntur</p>
  <div class="feat-icon" style="left:216px;top:146px;background:#6c6c6e"><svg width="10" height="10" viewBox="0 0 10 10"><path d="M5 0.5l1.4 3 3.1.3-2.4 2 .8 3.1L5 7.3 2.1 8.9l.8-3.1-2.4-2 3.1-.3z" fill="#fff"/></svg></div>
  <p class="feature" style="left:148px;top:202px;width:143px">Nemo enim ipsam voluptatem quia voluptas sit aspernatur aut</p>
  <div class="feat-icon" style="left:300px;top:193px;background:var(--red)"><svg width="8" height="10" viewBox="0 0 8 10"><path d="M1 0h4l2 2v8H1z" fill="#fff"/></svg></div>
  <p class="footer">Presentation Title &nbsp;|&nbsp; Jan 02,2025</p>
  <span class="page">09</span>
</section>

<!-- 3 Agenda -->
<section class="slide col-l framed" style="top:361px">
  <h2 class="s-title">AGENDA</h2>
  <div class="rule" style="left:0;top:36px;width:130px"></div>
  <span class="brand-mini">MARLOW PIKE</span>
  <ol class="agenda-list">
    <li><span class="num">01</span>LOREM IPSUM DOLOR SIT</li>
    <li><span class="num">02</span>LOREM IPSUM DOLOR SIT AMET, CONSECTETEA</li>
    <li><span class="num">03</span>LOREM IPSUM DOLOR SIT</li>
    <li><span class="num">04</span>LOREM IPSUM DOLOR SIT AMET, CONSECTETEA</li>
    <li><span class="num">05</span>LOREM IPSUM DOLOR SIT</li>
  </ol>
  <p class="footer">Presentation Title &nbsp;|&nbsp; Jan 02,2025</p>
  <span class="page">02</span>
</section>

<!-- 4 Title here -->
<section class="slide col-r framed" style="top:361px">
  <div class="deco deco-soft" style="left:140px;top:-10px;width:320px;height:270px" role="img" aria-label="Faint decorative emblem"></div>
  <span class="brand-mini">MARLOW PIKE</span>
  <h2 class="big-title" style="left:14px;top:103px">TITLE HERE</h2>
  <div class="rule" style="left:0;top:134px;width:150px"></div>
  <p class="footer">Presentation Title &nbsp;|&nbsp; Jan 02,2025</p>
</section>

<!-- 5 About us -->
<section class="slide col-l framed" style="top:624px">
  <div class="deco deco-dark" style="left:180px;top:-10px;width:280px;height:260px" role="img" aria-label="Large decorative emblem with red accent"></div>
  <h2 class="s-title">ABOUT US</h2>
  <div class="rule" style="left:0;top:36px;width:145px"></div>
  <span class="brand-mini">MARLOW PIKE</span>
  <p class="body-text" style="left:22px;top:54px;width:145px">Nemo enim ipsam voluptatem quia voluptas sit aspernatur aut odit aut fugit, sed quia consequuntur magni dolores eos qui ratione voluptatem sequi nesciunt. Neque porro quisquam est, qui dolorem ipsum quia dolor sit amet, consectetur, adipisci velit, sed quia non numquam eius modi tempora incidunt ut labore et dolore magnam aliquam quaerat voluptatemt enim ad minima veniam, quis nostrum exercitationem ullam corporis suscipit laboriosam.</p>
  <p class="footer">Presentation Title &nbsp;|&nbsp; Jan 02,2025</p>
  <span class="page">04</span>
</section>

<!-- 6 Meet our team -->
<section class="slide col-r framed" style="top:624px">
  <div class="photo" style="left:190px;top:0;width:249px;height:110px;background:linear-gradient(135deg,#d8dde3,#3b4a66 55%,#e9ecef)" role="img" aria-label="Photo of two colleagues reviewing documents at a desk"></div>
  <div class="deco deco-dark" style="left:210px;top:60px;width:260px;height:210px" role="img" aria-label="Decorative emblem with red accent"></div>
  <span class="brand-mini">MARLOW PIKE</span>
  <h2 class="s-title" style="left:16px;top:58px">MEET OUR<br>TEAM</h2>
  <div class="rule" style="left:0;top:110px;width:160px"></div>
  <p class="body-text" style="left:22px;top:126px;width:160px">Nemo enim ipsam voluptatem quia voluptas sit aspernatur aut odit aut fugit, sed quia consequuntur magni dolores eos qui ratione voluptatem sequi nesciunt. Neque porro quisquam est, qui dolorem ipsum quia dolor sit amet, consectetur, adipisci velit, sed quia non numquam eius modi tempora incidunt ut</p>
  <p class="footer">Presentation Title &nbsp;|&nbsp; Jan 02,2025</p>
</section>

<!-- 7 Title here -->
<section class="slide col-l framed" style="top:888px">
  <div class="deco deco-soft" style="left:120px;top:-10px;width:320px;height:270px" role="img" aria-label="Faint decorative emblem"></div>
  <span class="brand-mini">MARLOW PIKE</span>
  <h2 class="big-title" style="left:14px;top:100px">TITLE HERE</h2>
  <div class="rule" style="left:0;top:131px;width:150px"></div>
  <p class="footer">Presentation Title &nbsp;|&nbsp; Jan 02,2025</p>
</section>

<!-- 8 Problem statement -->
<section class="slide col-r framed" style="top:888px">
  <h2 class="s-title" style="left:16px">PROBLEM STATEMENT</h2>
  <div class="rule" style="left:0;top:42px;width:263px"></div>
  <span class="brand-mini">MARLOW PIKE</span>
  <p style="position:absolute;left:22px;top:95px;font-size:30px;font-weight:800;color:#5d5d5f;line-height:1.05">MARLOW<br>PIKE</p>
  <p class="body-text" style="left:207px;top:66px;width:208px">Nemo enim ipsam voluptatem quia voluptas sit aspernatur aut odit aut fugit, sed quia consequuntur magni dolores eos qui ratione voluptatem sequi nesciunt. Neque porro quisquam est, qui dolorem ipsum quia dolor sit amet, consectetur, adipisci velit, sed quia non numquam eius modi tempora incidunt ut labore et dolore magnam</p>
  <p class="body-text" style="left:207px;top:160px;width:208px">Nemo enim ipsam voluptatem quia voluptas sit aspernatur aut odit aut fugit, sed quia consequuntur magni dolores eos qui ratione voluptatem sequi nesque porro quisqolorem ipsum quia dolor</p>
  <p class="footer">Presentation Title &nbsp;|&nbsp; Jan 02,2025</p>
  <span class="page">11</span>
</section>

<!-- 9 Why choose us -->
<section class="slide col-l framed" style="top:1151px">
  <h2 class="s-title">WHY CHOOSE US</h2>
  <div class="rule" style="left:0;top:36px;width:230px"></div>
  <span class="brand-mini">MARLOW PIKE</span>
  <p class="body-text" style="left:22px;top:52px;width:193px">Nemo enim ipsam voluptatem quia voluptas sit aspernatur aut odit aut fugit, sed quia consequuntur magni dolores eos qui ratione voluptatem sequi nesciunt. Neque porro quisquam est, qui dolorem ipsum quia dolor sit amet, consectetur, adipisci velit, sed quia non numquam eius modi tempora incidunt ut labore et dolore magnam aliquam quaerat voluptatemt enim ad minima veniam, quis nostrum exercitationem ullam corpuscipit laboriosamnisi ut aliquidcommodi consequatuquis autem vel eum iure reprehenderit qui in ea voluptate velit esse quam nihil molestiae consequatur</p>
  <div style="position:absolute;left:240px;top:52px;width:170px;height:170px;border-radius:50%;border:3px solid #ddd;box-shadow:0 0 0 2px #6c6c6e"></div>
  <div style="position:absolute;left:248px;top:60px;width:154px;height:154px;border-radius:50%;background:var(--red);color:#fff;font-size:7px;line-height:1.5;text-align:center;padding:24px 22px">Nemo enim ipsam voluptatem quia voluptas sit aspernatur aut odit aut fugit, sed quia consequuntur magni dolores eos qui ratione voluptatem sequi nesciunt. Neque porro quisquam est, qui dolorem ipsum quia dolor sit amet, consectetur, adipisci velit, sed quia non numquam eius modi tempora</div>
  <p class="footer">Presentation Title &nbsp;|&nbsp; Jan 02,2025</p>
  <span class="page">04</span>
</section>

<!-- 10 Our team -->
<section class="slide col-r framed" style="top:1151px">
  <h2 class="s-title" style="left:16px">OUR TEAM</h2>
  <div class="rule" style="left:0;top:42px;width:130px"></div>
  <span class="brand-mini">MARLOW PIKE</span>
  <div class="cards">
    <div class="card"><div class="avatar" role="img" aria-label="Portrait photo"></div><span class="name">Owen Hale</span><span class="role">Project Leader</span></div>
    <div class="card"><div class="avatar" role="img" aria-label="Portrait photo"></div><span class="name">Dr Nina Ross</span></div>
    <div class="card active"><div class="avatar" role="img" aria-label="Portrait photo"></div><span class="name">Leo Carter</span></div>
    <div class="card"><div class="avatar" role="img" aria-label="Portrait photo"></div><span class="name">Max Turner AM</span></div>
    <div class="card"><div class="avatar" role="img" aria-label="Portrait photo"></div><span class="name">Ivy Morgan</span></div>
  </div>
  <div class="descs">
    <p class="card-desc">Lorem ipsum dolor sit amet, consectetur adipiscing elit, sed do eiusmod tempor incididunt ut labore et dolore magna aliqua.</p>
    <p class="card-desc">Lorem ipsum dolor sit amet, consectetur adipiscing elit, sed do eiusmod tempor incididunt ut labore et dolore magna aliqua.</p>
    <p class="card-desc">Lorem ipsum dolor sit amet, consectetur adipiscing elit, sed do eiusmod tempor incididunt ut labore et dolore magna aliqua.</p>
    <p class="card-desc">Lorem ipsum dolor sit amet, consectetur adipiscing elit, sed do eiusmod tempor incididunt ut labore et dolore magna aliqua.</p>
    <p class="card-desc">Lorem ipsum dolor sit amet, consectetur adipiscing elit, sed do eiusmod tempor incididunt ut labore et dolore magna aliqua.</p>
  </div>
  <p class="footer">Presentation Title &nbsp;|&nbsp; Jan 02,2025</p>
  <span class="page">12</span>
</section>

<!-- 11 Quote -->
<section class="slide col-l quote-slide" style="top:1415px">
  <span class="qmark" style="left:70px;top:58px">&ldquo;</span>
  <div style="position:absolute;left:78px;top:78px;width:2px;height:70px;background:var(--red)"></div>
  <div style="position:absolute;left:78px;top:148px;width:100px;height:2px;background:var(--red)"></div>
  <span class="qmark" style="left:185px;top:140px">&rdquo;</span>
  <p class="quote-text">"Lorem ipsum dolor sit amet, consectetur adipiscing elit, sed do eiusmod tempor incididunt ut labore et dolore magna alt eminim veniam"</p>
</section>

<!-- 12 Title here -->
<section class="slide col-r framed" style="top:1415px">
  <div class="deco deco-soft" style="left:140px;top:-10px;width:320px;height:270px" role="img" aria-label="Faint decorative emblem"></div>
  <span class="brand-mini">MARLOW PIKE</span>
  <h2 class="big-title" style="left:14px;top:103px">TITLE HERE</h2>
  <div class="rule" style="left:0;top:134px;width:150px"></div>
  <p class="footer">Presentation Title &nbsp;|&nbsp; Jan 02,2025</p>
</section>

<!-- 13 Our graph -->
<section class="slide col-l framed" style="top:1678px">
  <h2 class="s-title">OUR GRAPH</h2>
  <div class="rule" style="left:0;top:36px;width:182px"></div>
  <span class="brand-mini">MARLOW PIKE</span>
  <p class="body-text" style="left:22px;top:50px;width:395px">Nemo enim ipsam voluptatem quia voluptas sit aspernatur aut odit aut fugit, sed quia consequuntur magni dolores eos qui ratione voluptatem sequi nesciunt. Neque porro quisquam est, qui dolorem ipsum quia dolor sit amet, consectetur, adipisci velit, sed quia non numquam eius</p>
  <div class="chart">
    <div class="axis"><span>120</span><span>100</span><span>80</span><span>60</span><span>40</span><span>20</span><span>0</span></div>
    <div class="bars">
      <div class="bar"><span style="height:20%">20%</span></div>
      <div class="bar"><span style="height:42%">50%</span></div>
      <div class="bar"><span style="height:50%">60%</span></div>
      <div class="bar"><span style="height:25%">30%</span></div>
      <div class="bar"><span class="hl" style="height:67%">80%</span></div>
      <div class="bar"><span style="height:75%">90%</span></div>
      <div class="bar"><span style="height:25%">30%</span></div>
      <div class="bar"><span style="height:83%">100%</span></div>
      <div class="bar"><span style="height:58%">70%</span></div>
    </div>
  </div>
  <p class="footer">Presentation Title &nbsp;|&nbsp; Jan 02,2025</p>
  <span class="page">06</span>
</section>

<!-- 14 Timeline -->
<section class="slide col-r framed" style="top:1678px">
  <h2 class="s-title" style="left:16px">TIMELINE</h2>
  <div class="rule" style="left:0;top:42px;width:120px"></div>
  <span class="brand-mini">MARLOW PIKE</span>
  <p class="tl-label" style="left:68px;top:60px">Project Commences<br>Dec 24</p>
  <p class="tl-label" style="left:178px;top:60px">Inception &amp; vi<br>Dec 2023- Jan 2024</p>
  <p class="tl-label" style="left:274px;top:56px">Stakeholder Engagement<br>Jan 2023 - Feb 2024</p>
  <div class="tl-stem" style="left:109px;top:76px;height:28px"></div>
  <div class="tl-stem" style="left:218px;top:76px;height:28px"></div>
  <div class="tl-stem" style="left:314px;top:76px;height:28px"></div>
  <div class="tl-node" style="left:88px"><svg width="18" height="18" viewBox="0 0 18 18"><circle cx="9" cy="9" r="4" fill="none" stroke="var(--red)" stroke-width="1.5"/><circle cx="9" cy="9" r="7" fill="none" stroke="var(--red)" stroke-dasharray="2 2"/></svg></div>
  <div class="tl-node alt" style="left:140px"><svg width="18" height="18" viewBox="0 0 18 18"><rect x="3" y="3" width="12" height="12" fill="none" stroke="var(--red)" stroke-width="1.3"/><path d="M5 7h8M5 10h8M5 13h5" stroke="var(--red)"/></svg></div>
  <div class="tl-node" style="left:192px"><svg width="18" height="18" viewBox="0 0 18 18"><rect x="3" y="2" width="10" height="14" fill="none" stroke="var(--red)" stroke-width="1.3"/><circle cx="11" cy="11" r="3" fill="none" stroke="var(--red)"/></svg></div>
  <div class="tl-node alt" style="left:244px"><svg width="18" height="18" viewBox="0 0 18 18"><rect x="2" y="3" width="14" height="12" fill="none" stroke="var(--red)" stroke-width="1.3"/><path d="M4 12l3-3 3 2 4-5" fill="none" stroke="var(--red)"/></svg></div>
  <div class="tl-node" style="left:296px"><svg width="18" height="18" viewBox="0 0 18 18"><rect x="7" y="2" width="4" height="4" fill="none" stroke="var(--red)"/><rect x="2" y="12" width="4" height="4" fill="none" stroke="var(--red)"/><rect x="12" y="12" width="4" height="4" fill="none" stroke="var(--red)"/><path d="M9 6v3M4 12V9h10v3" fill="none" stroke="var(--red)"/></svg></div>
  <div class="tl-stem" style="left:166px;top:146px;height:30px"></div>
  <div class="tl-stem" style="left:270px;top:146px;height:30px"></div>
  <p class="tl-label" style="left:126px;top:178px">Development of Draft Plan<br>Feb-Mar 2024</p>
  <p class="tl-label" style="left:230px;top:178px">Final Report<br>Mar -Apr 2024</p>
  <p class="footer">Presentation Title &nbsp;|&nbsp; Jan 02,2025</p>
  <span class="page">13</span>
</section>

<!-- 15 Our infographics -->
<section class="slide col-l framed" style="top:1941px">
  <h2 class="s-title" style="left:16px">OUR INFOGRAPHICS</h2>
  <div class="rule" style="left:0;top:36px;width:245px"></div>
  <span class="brand-mini">MARLOW PIKE</span>
  <p class="body-text" style="left:22px;top:48px;width:395px">Nemo enim ipsam voluptatem quia voluptas sit aspernatur aut odit aut fugit, sed quia consequuntur magni dolores eos qui rationm quia dolor sit amet, consectesquia non numquam eius</p>
  <div class="info-box" style="left:48px"><svg width="10" height="14" viewBox="0 0 10 14"><rect x="1" y="0.5" width="8" height="13" rx="1.5" fill="var(--red)"/><circle cx="5" cy="11" r="1" fill="#fff"/></svg><h4>TITLE HERE</h4><p>Lorem ipsum dolor sit amet, consectetur adipiscing elit, sed do eiusmodtempor incididunt ut labore et dolore magna aliqua. Ut enim ad minim veniamLorem ipsum dolor sit amet, consectetur adipisicing elit.</p></div>
  <div class="info-box" style="left:165px"><svg width="16" height="14" viewBox="0 0 16 14"><rect x="1" y="1" width="14" height="9" fill="none" stroke="var(--red)" stroke-width="1.6"/><path d="M5 13h6M8 10v3" stroke="var(--red)" stroke-width="1.4"/></svg><h4>TITLE HERE</h4><p>Lorem ipsum dolor sit amet, consectetur adipiscing elit, sed do eiusmodtempor incididunt ut labore et dolore magna aliqua. Ut enim ad minim veniamLorem ipsum dolor sit amet, consectetur adipisicing elit.</p></div>
  <div class="info-box" style="left:292px"><svg width="18" height="12" viewBox="0 0 18 12"><path d="M4 11a3.5 3.5 0 010-7 5 5 0 019.5 1A3 3 0 0114 11z" fill="var(--red)"/></svg><h4>TITLE HERE</h4><p>Lorem ipsum dolor sit amet, consectetur adipiscing elit, sed do eiusmodtempor incididunt ut labore et dolore magna aliqua. Ut enim ad minim veniamLorem ipsum dolor sit amet, consectetur adipisicing elit.</p></div>
  <svg style="position:absolute;left:138px;top:130px" width="30" height="30" viewBox="0 0 30 30"><path d="M2 2v10a4 4 0 004 4h22M2 28v-8" fill="none" stroke="#9a9a9c" stroke-width="2"/></svg>
  <svg style="position:absolute;left:255px;top:135px" width="40" height="20" viewBox="0 0 40 20"><path d="M2 10h34M30 4l6 6-6 6" fill="none" stroke="#9a9a9c" stroke-width="2"/></svg>
  <p class="footer">Presentation Title &nbsp;|&nbsp; Jan 02,2025</p>
  <span class="page">07</span>
</section>

<!-- 16 Reporting -->
<section class="slide col-r framed" style="top:1941px">
  <h2 class="s-title" style="left:16px">REPORTING</h2>
  <div class="rule" style="left:0;top:42px;width:140px"></div>
  <span class="brand-mini">MARLOW PIKE</span>
  <p class="body-text" style="left:15px;top:56px;width:196px;font-size:6.4px;line-height:1.5">Lorem ipsum dolor sit amet, consectetur adipiscing elit, sed do eiusmod tempor incididunt ut labore et dolore magna aliqua. Ut enim ad minim veniam, quis nostrud exercitation ullamco laboris nisi ut aliquip ex ea<br><br>Sed ut perspiciatis unde omnis iste natus error sit voluptatem accusantium doloremque laudantium, totam rem aperiam, eaque ipsa quae ab illo inventore veritatis et quasi architecto beatae vitae dicta sunt explicabo. Nemo enim ipsam voluptatem quia voluptas sit aspernatur aut odit aut fugit, sed quia consequuntur magni dolores eos qui ratione voluptatem sequi nesciunt. Neque porro quisquam est, qui dolorem ipsum quia dolor sit amet.</p>
  <svg style="position:absolute;left:220px;top:50px" width="130" height="170" viewBox="0 0 130 170">
    <path d="M55 5a80 80 0 0160 35L85 58a45 45 0 00-30-18z" fill="var(--red)"/>
    <path d="M115 40a80 80 0 0112 45H92a45 45 0 00-7-27z" fill="#2e2e30"/>
    <path d="M127 85a80 80 0 01-12 45L85 112a45 45 0 007-27z" fill="var(--red)"/>
    <path d="M115 130a80 80 0 01-60 35v-35a45 45 0 0030-18z" fill="#2e2e30"/>
    <circle cx="55" cy="85" r="40" fill="#fff" stroke="#ddd" stroke-width="3"/>
    <text x="55" y="88" text-anchor="middle" font-family="Montserrat,sans-serif" font-size="8" font-weight="700" fill="#222">REPORTING</text>
    <text x="70" y="30" font-family="Montserrat,sans-serif" font-size="5" fill="#fff">Task 1:</text>
    <text x="102" y="70" font-family="Montserrat,sans-serif" font-size="5" fill="#fff">Task 2</text>
    <text x="102" y="108" font-family="Montserrat,sans-serif" font-size="5" fill="#fff">Task 3</text>
    <text x="68" y="150" font-family="Montserrat,sans-serif" font-size="5" fill="#fff">Task 4:</text>
  </svg>
  <p class="tl-label" style="left:352px;top:58px;text-align:left;width:70px;font-size:5px">Inception Situation Analysis</p>
  <p class="tl-label" style="left:352px;top:92px;text-align:left;width:80px;font-size:4.5px">Traditional Owner &amp; Stakeholder Consultation</p>
  <p class="tl-label" style="left:352px;top:140px;text-align:left;width:80px;font-size:4.5px">Utilisation Strategy Development &amp; Draft Plan</p>
  <p class="tl-label" style="left:352px;top:180px;text-align:left;width:60px;font-size:4.5px">Reporting</p>
  <p class="footer">Presentation Title &nbsp;|&nbsp; Jan 02,2025</p>
  <span class="page">14</span>
</section>

<!-- 17 What we do -->
<section class="slide col-l" style="top:2204px">
  <div class="wwd-panel"></div>
  <svg style="position:absolute;left:200px;top:0" width="70" height="246" viewBox="0 0 70 246"><path d="M30 0c30 60 30 180-10 246" fill="none" stroke="#8a8a8c" stroke-width="3"/></svg>
  <h2 class="s-title" style="left:16px;color:#fff">WHAT WE DO</h2>
  <div class="rule" style="left:0;top:36px;width:208px"></div>
  <span class="brand-mini">MARLOW PIKE</span>
  <div class="wwd-ico" style="left:28px;top:55px;background:#fff"><svg width="10" height="10" viewBox="0 0 10 10"><rect x="2" y="4" width="6" height="5" fill="none" stroke="#555"/><path d="M3 4V3a2 2 0 014 0v1" fill="none" stroke="#555"/></svg></div>
  <div class="wwd-item" style="left:62px;top:55px;width:135px;color:#ddd"><h5 style="color:#fff">Voluptatum deleniti</h5>Voluptatum deleniti atque corrupti quos dolores et quas molestias excepturi sint occaecati</div>
  <div class="wwd-ico" style="left:28px;top:113px;background:var(--red)"><svg width="10" height="10" viewBox="0 0 10 10"><path d="M2 8l1-3 4-4 2 2-4 4z" fill="none" stroke="#fff"/></svg></div>
  <div class="wwd-item" style="left:62px;top:113px;width:135px;color:#eee"><h5 style="color:#fff">Raesentium volupt</h5>Voluptatum deleniti atque corrupti quos dolores et quas molestias epturi sint occaecati cupiditate non</div>
  <div class="wwd-ico" style="left:28px;top:172px;background:#fff"><svg width="10" height="10" viewBox="0 0 10 10"><path d="M2 1h4l2 2v6H2z" fill="none" stroke="#555"/></svg></div>
  <div class="wwd-item" style="left:62px;top:172px;width:135px;color:#fff"><h5>Raesentium volupt</h5>Voluptatum deleniti atque corrupti quos dolores et quas molestias xcepturi sint occaecati</div>
  <div class="wwd-ico" style="left:231px;top:50px;background:var(--red)"><svg width="10" height="10" viewBox="0 0 10 10"><ellipse cx="5" cy="2.5" rx="3.5" ry="1.5" fill="none" stroke="#fff"/><path d="M1.5 2.5v5c0 1 7 1 7 0v-5" fill="none" stroke="#fff"/></svg></div>
  <div class="wwd-item" style="left:262px;top:48px;width:150px;color:#666"><h5 style="color:#222">Raesentium volupt</h5>Voluptatum deleniti atque corrupti quos dolores et quas molestias excepturi sint occaecati cupiditate non provident.</div>
  <div class="wwd-ico" style="left:220px;top:113px;background:#3a3a3c"><svg width="10" height="10" viewBox="0 0 10 10"><circle cx="5" cy="3" r="2" fill="none" stroke="#fff"/><path d="M1 9a4 4 0 018 0" fill="none" stroke="#fff"/></svg></div>
  <div class="wwd-item" style="left:251px;top:111px;width:150px;color:#666"><h5 style="color:#222">Raesentium volupt</h5>Voluptatum deleniti atque corrupti quos dolores et quas molestias excepturi sint occaecati cupiditate non provident.</div>
  <div class="wwd-ico" style="left:203px;top:172px;background:var(--red)"><svg width="10" height="10" viewBox="0 0 10 10"><rect x="1" y="2" width="8" height="5" fill="none" stroke="#fff"/><path d="M3 9h4" stroke="#fff"/></svg></div>
  <div class="wwd-item" style="left:233px;top:170px;width:150px;color:#666"><h5 style="color:#222">Raesentium volupt</h5>Voluptatum deleniti atque corrupti quos dolores et quas molestias excepturi sint occaecati cupiditate non provident,</div>
  <p class="footer" style="color:#f2b7bf">Presentation Title &nbsp;|&nbsp; Jan 02,2025</p>
  <span class="page">08</span>
</section>

<!-- 18 Thank you (grey) -->
<section class="slide col-r thanks-grey" style="top:2204px">
  <p style="position:absolute;left:0;right:0;top:44px;text-align:center;font-size:30px;font-weight:800;color:#fff;line-height:1.05">MARLOW<br>PIKE</p>
  <div class="rule" style="left:95px;top:135px;width:250px"></div>
  <p style="position:absolute;left:0;right:0;top:148px;text-align:center;font-size:30px;font-weight:800;color:#fff">THANK <span style="color:var(--red)">YOU</span></p>
  <div style="position:absolute;left:35px;top:229px;width:370px;height:17px;background:var(--red);border-radius:9px 9px 0 0;display:flex;align-items:center;justify-content:center;gap:8px;font-size:6px;color:#fff;font-weight:600">
    <span>&#9990; Call Us : +1 555 014 2200</span><span>|</span><span>&#9993; hello@marlowpike.com</span>
    <span style="display:flex;gap:3px;margin-left:36px"><i style="width:8px;height:8px;border-radius:50%;background:#fff"></i><i style="width:8px;height:8px;border-radius:50%;background:#fff"></i><i style="width:8px;height:8px;border-radius:50%;background:#fff"></i></span>
  </div>
</section>

<!-- 19 Thank you (red) -->
<section class="slide thanks-red" style="top:2466px;left:381px">
  <div class="deco" style="left:235px;top:40px;width:180px;height:150px;background:radial-gradient(circle at 60% 55%,#fff 0 10%,#9e9ea0 11% 40%,rgba(255,255,255,0) 65%)" role="img" aria-label="Decorative emblem in grey and white"></div>
  <p style="position:absolute;left:26px;top:14px;font-size:17px;font-weight:800;color:#e7c2c7;line-height:1.05">MARLOW<br>PIKE</p>
  <p style="position:absolute;left:18px;top:67px;font-size:19px;font-weight:800;color:#fff">THANK YOU</p>
  <div style="position:absolute;left:0;top:93px;width:210px;height:1px;background:#fff"></div>
  <div class="contact-row" style="top:112px"><i><svg width="8" height="8" viewBox="0 0 8 8"><path d="M1 1l2 0 1 2-1 1a4 4 0 002 2l1-1 2 1v2C4 8 0 4 1 1z" fill="var(--red)"/></svg></i>+1 (555) 014 2200</div>
  <div class="contact-row" style="top:138px"><i><svg width="8" height="6" viewBox="0 0 8 6"><rect width="8" height="6" fill="var(--red)"/><path d="M0 0l4 3 4-3" fill="none" stroke="#fff" stroke-width=".8"/></svg></i>info@marlowpike.com</div>
  <div class="contact-row" style="top:164px"><i><svg width="6" height="8" viewBox="0 0 6 8"><path d="M3 8S0 4.5 0 3a3 3 0 016 0c0 1.5-3 5-3 5z" fill="var(--red)"/><circle cx="3" cy="3" r="1" fill="#fff"/></svg></i>465, Lorum Ipsum Dolore Sed, United States</div>
  <div class="contact-row" style="top:190px"><i><svg width="8" height="8" viewBox="0 0 8 8"><circle cx="4" cy="4" r="3.5" fill="none" stroke="var(--red)"/><path d="M0.5 4h7M4 .5c-2 2-2 5 0 7M4 .5c2 2 2 5 0 7" fill="none" stroke="var(--red)" stroke-width=".6"/></svg></i>www.marlowpike.com</div>
</section>

</body>
</html>
```